Need a stunning looking Business Card Design for my Telecom Business, Wow FACTOR!

I deal with high level IT Directors , and Contractors.
I need to impress them with a sleek , professional and unique business card.
Im thinking options as far as rounded edges, plastic , or even metal card or die cut on a corner.
Whatever looks better and leave an unforgettable first impression.
im looking for the wow factor.
Front should have the basics info (attached on the picture of current business card)
i would like to add picture of myself somewhere
Back side
should have logo and maybe some pictures or past projects, you can download from my website ( www.brivelgroup.com)

```html
<!DOCTYPE html>
<html lang="en">
<head>
<meta charset="utf-8">
<title>Brivel Group – Business Card</title>
<link href="https://fonts.googleapis.com/css2?family=Montserrat:wght@400;500;600;700&display=swap" rel="stylesheet">
<style>
  :root{
    --backdrop:#a8a8a8;
    --card-white:#ffffff;
    --navy:#1b2a52;
    --navy-deep:#161b36;
    --cyan:#22a9e6;
    --ink:#1f2233;
    --photo-top:#2c4a80;
    --photo-bottom:#8a8f9c;
  }
  *{margin:0;padding:0;box-sizing:border-box}
  html,body{width:900px;height:1200px;overflow:hidden}
  body{background:var(--backdrop);font-family:"Montserrat",sans-serif;position:relative;color:var(--ink)}
  .card{position:absolute;left:80px;width:742px;height:440px;border-radius:24px;overflow:hidden}
  .card--front{top:130px;background:var(--card-white)}
  .card--back{top:638px;background:var(--navy-deep)}

  .brand{position:absolute;display:flex;align-items:center;gap:14px;font-weight:600;letter-spacing:2px}
  .brand__dot{width:16px;height:16px;border-radius:50%}
  .card--front .brand{left:42px;top:180px;font-size:34px;color:var(--navy)}
  .card--front .brand__dot{background:var(--navy)}
  .card--back .brand{left:0;right:0;top:185px;justify-content:center;font-size:46px;color:#fff}
  .card--back .brand__dot{background:#fff;width:20px;height:20px}

  .portrait{position:absolute;left:520px;top:35px;width:180px;height:208px;border-radius:18px;
    background:linear-gradient(180deg,var(--photo-top) 0%,var(--photo-top) 55%,var(--photo-bottom) 100%)}

  .name-band{position:absolute;left:425px;top:270px;width:317px;height:53px;background:var(--navy);
    clip-path:polygon(40px 0,100% 0,100% 100%,0 100%);text-align:right;padding-right:25px;padding-top:4px}
  .name-band__name{color:var(--cyan);font-weight:700;font-size:23px;letter-spacing:.5px;line-height:26px}
  .name-band__role{color:#fff;font-size:15px;font-weight:500;line-height:18px}

  .license{position:absolute;left:43px;top:294px;font-size:15px;font-weight:500}
  .license-rule{position:absolute;left:42px;top:321px;width:400px;height:2px;background:var(--navy)}

  .contacts{position:absolute;left:38px;top:343px;list-style:none}
  .contacts li{display:flex;align-items:center;height:21px;font-size:16px;font-weight:500}
  .contacts svg{width:14px;height:14px;margin-right:18px;fill:var(--navy)}

  .office{position:absolute;right:28px;top:341px;text-align:right}
  .office__company{font-weight:600;font-size:18px;color:var(--navy);line-height:24px;margin-bottom:4px}
  .office__area{font-size:15px;line-height:21px}
</style>
</head>
<body>
  <section class="card card--front">
    <div class="brand"><span class="brand__dot"></span>BRIVEL GROUP</div>
    <div class="portrait" role="img" aria-label="Portrait photo of Kenji Arlow"></div>
    <div class="name-band">
      <div class="name-band__name">KENJI ARLOW</div>
      <div class="name-band__role">Operation Manager</div>
    </div>
    <div class="license">State License #ES19004820</div>
    <div class="license-rule"></div>
    <ul class="contacts">
      <li><svg viewBox="0 0 24 24"><path d="M6.6 10.8a15 15 0 0 0 6.6 6.6l2.2-2.2a1 1 0 0 1 1-.25 11 11 0 0 0 3.6.6 1 1 0 0 1 1 1V20a1 1 0 0 1-1 1A17 17 0 0 1 3 4a1 1 0 0 1 1-1h3.5a1 1 0 0 1 1 1c0 1.25.2 2.45.6 3.6a1 1 0 0 1-.25 1z"/></svg>954) 555-0148</li>
      <li><svg viewBox="0 0 24 24"><path d="M2 5h20v2l-10 6L2 7z M2 9l10 6 10-6v10H2z"/></svg>info@brivelgroup.com</li>
      <li><svg viewBox="0 0 24 24"><circle cx="12" cy="12" r="10"/></svg>www.brivelgroup.com</li>
    </ul>
    <div class="office">
      <div class="office__company">Brivel Group</div>
      <div class="office__area">Offices in Miami, Browards</div>
      <div class="office__area">&amp; Palm Beach</div>
    </div>
  </section>

  <section class="card card--back">
    <div class="brand"><span class="brand__dot"></span>BRIVEL GROUP</div>
  </section>
</body>
</html>
```